Technical audit needs a report template

As our company runs various technical audits, we also provide findings on paper, online or in Powerpoint. For this reason we need an identity pack, which includes business cards, complimentary cards, letterhead and the likes.

Who would be up to create this stationery pack for us? We hope to receive a style for these documents, that look professional and can be easily extended.
Updates

Project Deadline Extended Reason: I would like to provide the opportunity to friended designers to submit their designs too! Added Sunday, October 9, 2016

Target Market(s)

Start-ups, scale-ups and investors

Industry/Entity Type

Investment

Contact Information for Business Card

Street: Lindenhoutkade 42
Postcode: 3617KW
City: Utrecht
Country: The Netherlands
Phone: +31 302849516
Cell Phone: +31 6 58193074
email: jeroen@vexomari.example
website: https://vexomari.example

Requirements
Must have
• I don't have inspiration, should just be a slick design based on the logo provided.
Nice to have
• Logo could be on the back of the card?
Should not have
• Should not use different colours then the logo, or at least fit the colour scheme.

```html
<!DOCTYPE html>
<html lang="en">
<head>
<meta charset="utf-8">
<title>Jeroen – Auditor business card</title>
<link rel="stylesheet" href="https://fonts.googleapis.com/css2?family=Montserrat:wght@400&family=Open+Sans:wght@400&display=swap">
<style>
  :root {
    --paper: #ffffff;
    --ink: #1a1a1a;
    --blue-deep: #00a6d6;
    --blue-light: #4cc3ee;
  }
  html, body {
    margin: 0;
    padding: 0;
    overflow: hidden;
    background: var(--paper);
  }
  .card {
    position: relative;
    width: 1200px;
    height: 690px;
    background: var(--paper);
    overflow: hidden;
  }
  .brand-graphic {
    position: absolute;
    left: 0;
    top: 0;
    width: 560px;
    height: 690px;
    background: linear-gradient(135deg, var(--blue-light) 0%, var(--blue-deep) 100%);
  }

  .contact {
    position: absolute;
    top: 10px;
    left: 778px;
    right: 6px;
    margin: 0;
    display: grid;
    grid-template-columns: auto 1fr;
    column-gap: 16px;
    font-family: "Open Sans", sans-serif;
    font-size: 22px;
    line-height: 27px;
  }
  .contact dt {
    color: var(--blue-deep);
    margin: 0;
  }
  .contact dd {
    color: var(--ink);
    margin: 0;
    text-align: right;
  }

  .identity {
    position: absolute;
    left: 577px;
    top: 226px;
    width: 382px;
  }
  .name {
    margin: 0;
    font-family: "Montserrat", sans-serif;
    font-weight: 400;
    font-size: 88px;
    line-height: 1;
    letter-spacing: 1px;
    color: var(--ink);
    white-space: nowrap;
  }
  .name .accent { color: var(--blue-deep); }

  .role {
    margin: 4px 0 0;
    font-family: "Open Sans", sans-serif;
    font-weight: 400;
    font-size: 38px;
    line-height: 1;
    text-align: right;
    color: var(--ink);
  }
</style>
</head>
<body>
<main class="card">
  <div class="brand-graphic" role="img" aria-label="Company brand graphic in light and deep blue"></div>

  <dl class="contact">
    <dt>phone</dt><dd>+31 302849516</dd>
    <dt>cellphone</dt><dd>+31 6 58193074</dd>
    <dt>email</dt><dd>jeroen@vexomari.example</dd>
  </dl>

  <div class="identity">
    <h1 class="name">JER<span class="accent">OEN</span></h1>
    <p class="role">Auditor</p>
  </div>
</main>
</body>
</html>
```